Business Identity Stationary

Already have the logo which is in the attached files so only need the Business STationary
1) Double Sided Business Card
2) Letterhead
3) Presentation folder with business card holder on inside cover
4) WIth compliments slip
See information for business cards, letterhead and presentation folder below.
http://files.pixelbazaar-example.com/img/771204/40612/40612_3918825_771204_thumb.jpg
Updates

This should be a simply job using a logo we already had designed along with a little device. I suggest using the device off center and perhaps lower in the corner in an abstract way. Also the logo device could be used as a watermark for the letterhead. The designer who created the logo presented something that I think works well for a business card. The front of the double sided business card could have the name logo small for the website address and only use the Lime device on the front. Then on the back could be the name Brevar Consulting logo.

Please note that for the business card the black and lime green background do look good. Also please think of using the lime device separately in an unusual way.

It has been brought to my attention that.my budget was far to low. Hopefully this.will attract you to the project. 

The parent company of Brevar Consulting is TallHeron investments. I have uploaded a file of the Tall Heron business card I really like. Perhaps use this business card as a guide to the type of modern and clean style I am looking for. It also works to have the Brevar Consultign and Tall Heron similar.

Reason: Still haven't received anything exactly right.

Industry/Entity Type

Business

Font styles to use
Sans Serif

Colors
9bcb3c
000000
5c5c5c
add136
cadf82
eaf2cf
f9fbf2
1b1b1b
757575

Requirements
Must have
• 1) Double Sided Business Card
Marta Delvorin
Director
Tel: +505 8290 3357
Email: mkd@brevarconsulting-example.com
Website: www.brevarconsulting-example.com

Everett Delvorin
Director
Tel: +505 8290 3362
Email: ekd@brevarconsulting-example.com

Lucia Pardo Ventrosa
Director
Tel: 8442 6183
Email: lpv@brevarconsulting-example.com

2) Letterhead
Logo
Lime Logo Device
Website Address: www.brevarconsulting-example.com
Small print on bottom: Brevar Consulting a Tall Heron Investment Company SA. RUC K0720000483915

3) Presentation Folder
Traditional Presentation folder with inside front cover spot for the insertion of business card.

4) With Compliments slip

```html
<!DOCTYPE html>
<html lang="en">
<head>
<meta charset="utf-8">
<title>Brevar Consulting — Stationery Set</title>
<link href="https://fonts.googleapis.com/css2?family=Quicksand:wght@400;500&display=swap" rel="stylesheet">
<style>
  :root{
    --lime:#add136;
    --lime-soft:#cadf82;
    --lime-pale:#eaf2cf;
    --black:#000000;
    --ink:#1b1b1b;
    --grey:#5c5c5c;
    --grey-mid:#757575;
    --grey-light:#c4c9c9;
    --paper:#ffffff;
    --backdrop:#9aa5a6;
    --font:"Quicksand", sans-serif;
  }
  *{box-sizing:border-box;margin:0;padding:0}
  html,body{width:1200px;height:900px;overflow:hidden}
  body{background:var(--backdrop);font-family:var(--font);position:relative}

  .sheet{position:absolute;overflow:hidden;box-shadow:0 6px 18px rgba(0,0,0,.25)}
  .wordmark{display:flex;align-items:center;gap:6px;color:var(--paper);font-weight:400;white-space:nowrap;letter-spacing:.02em}
  .wordmark .dot{border-radius:50%;background:var(--lime);flex:none}

  /* Letterhead */
  .letterhead{left:125px;top:30px;width:345px;height:487px;background:var(--paper)}
  .letterhead .header{height:40px;background:var(--black);display:flex;align-items:center;padding-left:16px}
  .letterhead .header .wordmark{font-size:12px}
  .letterhead .header .dot{width:8px;height:8px}
  .letterhead .decor{position:absolute;left:0;top:40px}
  .letterhead .footer{position:absolute;left:0;bottom:0;width:100%;height:26px;background:var(--ink);color:var(--paper);font-size:5.4px;display:flex;align-items:center;padding-left:12px}

  /* Presentation folder */
  .folder-cover{left:500px;top:60px;width:290px;height:430px;background:var(--ink)}
  .folder-cover .decor{position:absolute;left:0;top:0}
  .folder-cover .wordmark{position:absolute;right:22px;bottom:26px;font-size:17px}
  .folder-cover .dot{width:12px;height:12px}

  .folder-inside{left:800px;top:60px;width:290px;height:430px;background:var(--paper)}
  .folder-inside .header{height:34px;background:var(--black)}
  .folder-inside .decor{position:absolute;left:0;top:34px}
  .folder-inside .card-slot{position:absolute;left:22px;bottom:40px;width:110px;height:66px;border:1px solid var(--grey-light);border-top:none}

  /* Business cards */
  .card{top:560px;width:105px;height:170px;background:var(--black)}
  .card-front{left:140px}
  .card-front .wordmark{position:absolute;left:12px;top:48px;font-size:10px}
  .card-front .dot{width:8px;height:8px}
  .card-front .badge{position:absolute;left:6px;bottom:8px;width:26px;height:26px;border-radius:50%;background:var(--lime)}
  .card-front .strip{position:absolute;left:38px;right:0;bottom:18px;height:7px;background:var(--grey);color:var(--paper);font-size:3.6px;line-height:7px;padding-left:4px}

  .card-back{left:260px;background:var(--ink)}
  .card-back .wordmark{position:absolute;left:10px;top:34px;font-size:10px}
  .card-back .dot{width:8px;height:8px}
  .card-back .details{position:absolute;left:10px;top:88px;color:var(--paper);font-size:5px;line-height:1.55}
  .card-back .details .name{font-size:6px;font-weight:500}
  .card-back .details .role{color:var(--lime)}

  /* With compliments slip */
  .slip{left:500px;top:540px;width:330px;height:150px;background:var(--paper)}
  .slip .header{height:36px;background:var(--black);display:flex;align-items:center;padding-left:12px}
  .slip .header .wordmark{font-size:11px}
  .slip .header .dot{width:7px;height:7px}
  .slip .decor{position:absolute;right:0;top:0}
  .slip .greeting{position:absolute;left:12px;top:104px;font-size:7px;color:var(--ink);font-weight:500}
  .slip .footer{position:absolute;left:0;bottom:0;width:100%;height:24px;background:var(--ink);color:var(--paper);font-size:5.4px;display:flex;align-items:center;padding-left:12px}

  /* Brand sign-off */
  .signoff{position:absolute;right:40px;bottom:40px}
  .signoff .wordmark{font-size:40px;gap:14px}
  .signoff .dot{width:30px;height:30px}
</style>
</head>
<body>

<section class="sheet letterhead" aria-label="Letterhead">
  <header class="header"><span class="wordmark">Brevar Consulting<span class="dot"></span></span></header>
  <svg class="decor" width="345" height="421" viewBox="0 0 345 421" aria-hidden="true">
    <rect x="230" y="40" width="115" height="300" fill="var(--grey-light)"/>
  </svg>
  <footer class="footer">www.brevarconsulting-example.com &nbsp;|&nbsp; Brevar Consulting a Tall Heron Investment Company SA. RUC K0720000483915</footer>
</section>

<section class="sheet folder-cover" aria-label="Presentation folder, front cover">
  <svg class="decor" width="290" height="430" viewBox="0 0 290 430" aria-hidden="true">
    <rect x="20" y="90" width="180" height="290" fill="#141414"/>
    <rect x="60" y="150" width="110" height="170" fill="#1f1f1f"/>
  </svg>
  <span class="wordmark">Brevar Consulting<span class="dot"></span></span>
</section>

<section class="sheet folder-inside" aria-label="Presentation folder, inside with business card slot">
  <div class="header"></div>
  <svg class="decor" width="290" height="396" viewBox="0 0 290 396" aria-hidden="true">
    <rect x="0" y="0" width="40" height="396" fill="var(--grey-light)"/>
    <rect x="190" y="80" width="100" height="190" fill="var(--lime-pale)"/>
    <rect x="190" y="300" width="100" height="96" fill="var(--lime)"/>
  </svg>
  <div class="card-slot"></div>
</section>

<section class="sheet card card-front" aria-label="Business card, front">
  <span class="wordmark">Brevar Consulting<span class="dot"></span></span>
  <div class="badge"></div>
  <div class="strip">www.brevarconsulting-example.com</div>
</section>

<section class="sheet card card-back" aria-label="Business card, back">
  <span class="wordmark">Brevar Consulting<span class="dot"></span></span>
  <div class="details">
    <p class="name">Marta Delvorin</p>
    <p class="role">Director</p>
    <p>Tel: +505 8290 3357</p>
    <p>mkd@brevarconsulting-example.com</p>
    <p>www.brevarconsulting-example.com</p>
  </div>
</section>

<section class="sheet slip" aria-label="With compliments slip">
  <header class="header"><span class="wordmark">Brevar Consulting<span class="dot"></span></span></header>
  <svg class="decor" width="110" height="126" viewBox="0 0 110 126" aria-hidden="true">
    <rect x="0" y="36" width="110" height="90" fill="var(--black)"/>
    <rect x="18" y="40" width="80" height="62" fill="var(--lime)"/>
  </svg>
  <p class="greeting">With Compliments</p>
  <footer class="footer">+505 8290 3357 &nbsp;|&nbsp; mkd@brevarconsulting-example.com &nbsp;|&nbsp; www.brevarconsulting-example.com</footer>
</section>

<div class="signoff"><span class="wordmark">Brevar Consulting<span class="dot"></span></span></div>

</body>
</html>
```